Halvern Guildworks Business Cards
Need out-of-the-box business card design
Halvern Guildworks Business Cards -
Creative Brief
Modern
Peter Strandquell
5172 Orrin St. Denver, CO 80219
peter@halvernguildworks.com
halvernguildworks.com
We exist to foster healthy artist Community, create points of Collaboration and provide tangible benefit to local Causes.

```html
<!DOCTYPE html>
<html lang="en">
<head>
<meta charset="utf-8">
<title>Halvern Guildworks Business Cards</title>
<link rel="stylesheet" href="https://fonts.googleapis.com/css2?family=Noto+Serif:wght@400;700&display=swap">
<style>
  :root {
    --bg: #e9e6df;
    --card: #ffffff;
    --olive: #7d8b2c;
    --gold: #b8962a;
    --gold-dark: #9c7c1c;
    --gold-light: #d2b24a;
    --ink: #3a3a36;
    --rule: #d9d6cc;
  }
  * { margin: 0; padding: 0; box-sizing: border-box; }
  html, body { width: 1200px; height: 852px; overflow: hidden; }
  body {
    background: var(--bg);
    font-family: "Noto Serif", Georgia, serif;
    color: var(--ink);
    position: relative;
  }
  .card {
    position: absolute;
    width: 520px;
    height: 300px;
    background: var(--card);
    border-radius: 18px;
    overflow: hidden;
    box-shadow: 0 6px 18px rgba(0,0,0,.18);
  }
  .card--front { left: 90px; top: 110px; }
  .card--back  { left: 590px; top: 440px; }

  .brand { display: flex; align-items: center; gap: 12px; }
  .brand__dot { width: 34px; height: 34px; border-radius: 50%; background: var(--gold); flex: none; }
  .brand__name {
    color: var(--olive);
    font-weight: 400;
    font-size: 30px;
    line-height: 1.05;
    text-transform: lowercase;
  }

  .card--front .brand { position: absolute; left: 40px; top: 40px; }

  .contact { font-size: 11px; line-height: 1.6; }
  .contact__name { color: var(--gold); font-weight: 700; font-size: 16px; margin-bottom: 10px; }
  .contact__line { display: flex; align-items: center; gap: 5px; }
  .contact__line svg { width: 11px; height: 11px; flex: none; }

  .card--front .contact { position: absolute; left: 118px; top: 150px; }
  .card--front .contact__row { display: flex; gap: 14px; }

  .band {
    position: absolute; left: 0; right: 0; bottom: 0; height: 42px;
    background: linear-gradient(180deg, var(--gold-light), var(--gold) 55%, var(--gold-dark));
    border-top: 4px solid #fff;
    box-shadow: 0 -2px 0 var(--gold-light);
    display: flex; align-items: center; justify-content: center;
  }
  .band__web { color: #fff; font-size: 12px; letter-spacing: 1.5px; }

  .card--back .brand { position: absolute; left: 36px; top: 102px; width: 200px; }
  .card--back .brand__name { font-size: 26px; }
  .divider {
    position: absolute; left: 262px; top: 0; bottom: 42px; width: 1px;
    background: linear-gradient(180deg, transparent, var(--rule) 20%, var(--rule) 80%, transparent);
  }
  .card--back .contact { position: absolute; left: 286px; top: 48px; }
  .card--back .contact__block { margin-bottom: 14px; }
</style>
</head>
<body>
  <section class="card card--front">
    <div class="brand">
      <span class="brand__dot"></span>
      <span class="brand__name">halvern<br>guildworks</span>
    </div>
    <div class="contact">
      <p class="contact__name">Peter Strandquell</p>
      <p>5172 Orrin St., Denver, CO 80219</p>
      <div class="contact__row">
        <p class="contact__line">
          <svg viewBox="0 0 12 12"><path d="M3 1l2 2.5-1.2 1.3a7 7 0 0 0 3.4 3.4L8.5 7 11 9l-1 2C5 11 1 7 1 2z" fill="var(--gold)"/></svg>
          3035550198
        </p>
        <p class="contact__line">
          <svg viewBox="0 0 12 12"><rect x="1" y="2.5" width="10" height="7" rx="1" fill="var(--gold)"/><path d="M1.5 3l4.5 3.5L10.5 3" stroke="#fff" fill="none"/></svg>
          peter@halvernguildworks.com
        </p>
      </div>
    </div>
    <div class="band"><span class="band__web">www.halvernguildworks.com</span></div>
  </section>

  <section class="card card--back">
    <div class="brand">
      <span class="brand__dot"></span>
      <span class="brand__name">halvern<br>guildworks</span>
    </div>
    <div class="divider"></div>
    <div class="contact">
      <p class="contact__name">Peter Strandquell</p>
      <div class="contact__block">
        <p>5172 Orrin St.</p>
        <p>Denver, CO 80219</p>
      </div>
      <p class="contact__line">
        <svg viewBox="0 0 12 12"><path d="M3 1l2 2.5-1.2 1.3a7 7 0 0 0 3.4 3.4L8.5 7 11 9l-1 2C5 11 1 7 1 2z" fill="var(--gold)"/></svg>
        3035550198
      </p>
      <p class="contact__line">
        <svg viewBox="0 0 12 12"><rect x="1" y="2.5" width="10" height="7" rx="1" fill="var(--gold)"/><path d="M1.5 3l4.5 3.5L10.5 3" stroke="#fff" fill="none"/></svg>
        peter@halvernguildworks.com
      </p>
    </div>
    <div class="band"><span class="band__web">www.halvernguildworks.com</span></div>
  </section>
</body>
</html>
```